PRISM LED video wall education flyer

Halvorn Signal Works are a specialist Audio Visual solutions integrator based in Australia. We sell a brand of LED video walls under the brand of PRISM, with our largest target market within the education sector. We need a two page brochure that we intend to have printed and also email (pdf) promoting a complete package price for our solution into education. The target market for this will be school principals and assistant principals wishing to install a large screen display into their school auditorium or gymnasium. Our PRISM LED video screens have now been installed into over 100 schools across Australia and we are leading the market based on the high performance, high brightness and our offer to design, supply install and maintain the product. our web site address
for the PRISM product is www.prismpanelscreens.example and website address for Halvorn signal works is www.halvornworks.example.au

Target Market(s)

School principals and assistant principals

Industry/Entity Type

Education

Colors
0054AA
0677BA
7BADD7
CADEEF
E8F1F8

Requirements
Must have
• PRISM Logo, Halvorn Signal Works Logo, a concise image of what we are offering which the large BIG screen LED video wall for school gyms, the package needs to show the 2 x speakers, QT720 video processor, wall cabinet, amplifier, HDMI socket and cabling including installation for only $35,500 ex tax. Page 2 needs to have the copy included int he attachments and needs to be layed out neatly, maybe some additional photos or images
Nice to have
• a professional flow of information and nice layout with emphasis on the large screen LED video wall - this is what we are selling. We also offer a free on-site demonstration which can be the call to action

```html
<!DOCTYPE html>
<html lang="en">
<head>
<meta charset="utf-8">
<title>PRISM LED Video Wall for Schools – Flyer</title>
<link href="https://fonts.googleapis.com/css2?family=Poppins:wght@300;400;500;600;700;800;900&display=swap" rel="stylesheet">
<style>
:root{
  --red:#ed1c24;
  --ink:#111111;
  --dark:#1d1d1d;
  --grey:#8c8c8c;
  --line:#c9c9c9;
  --paper:#ffffff;
  --backdrop:#c4c4c4;
  --photo-warm:#6b4a33;
  --photo-cool:#2a3c6e;
}
*{box-sizing:border-box;margin:0;padding:0}
html,body{width:1200px;height:1189px;overflow:hidden}
body{background:var(--backdrop);font-family:"Poppins",sans-serif;color:var(--ink);position:relative}
.page{position:absolute;top:255px;width:512px;height:663px;background:var(--paper);overflow:hidden}
.page--front{left:66px}
.page--back{left:617px}
.abs{position:absolute}
.footer-bar{position:absolute;left:0;bottom:0;width:100%;height:9px;background:var(--ink)}

/* front hero */
.hero{position:absolute;left:0;top:0;width:512px;height:234px;overflow:hidden}
.hero-photo{position:absolute;inset:0;background:linear-gradient(180deg,#e9e6e2 0%,#cfc6bb 20%,#8a6244 70%,var(--photo-warm) 100%)}
.hero-screen{position:absolute;left:222px;top:39px;width:257px;height:144px;background:linear-gradient(180deg,#3b4fa0 0%,#6a5fb5 30%,#c9774d 45%,#2d3f8a 60%,#1e2c6b 100%);border:2px solid #222}
.hero-shape{position:absolute;inset:0}
.brand-mark{position:absolute;left:33px;top:26px;color:#fff;font-weight:800;font-size:22px;letter-spacing:1px;line-height:1}
.brand-sub{position:absolute;left:34px;top:49px;color:var(--red);font-weight:700;font-size:7.5px;letter-spacing:2.6px}
.kicker{position:absolute;left:33px;top:78px;color:#fff;font-weight:400;font-size:12.5px;letter-spacing:3.6px}
.headline-brand{position:absolute;left:31px;top:88px;color:var(--red);font-weight:800;font-size:41px;line-height:1;letter-spacing:0.5px}
.headline-led{position:absolute;left:31px;top:127px;color:#fff;font-weight:800;font-size:41px;line-height:1}
.headline-wall{position:absolute;left:32px;top:168px;color:#fff;font-weight:800;font-size:25px;line-height:1}
.headline-for{position:absolute;left:33px;top:198px;color:#fff;font-weight:400;font-size:12.5px;letter-spacing:6.6px}

/* price */
.price-lead{position:absolute;left:31px;top:248px;font-size:12px;line-height:15px;font-weight:700}
.price-lead span{font-weight:400}
.price-box{position:absolute;left:124px;top:247px;width:115px;height:46px;background:var(--red);border-radius:4px;color:#fff;padding:2px 0 0 13px}
.price-box b{display:block;font-size:21px;font-weight:700;line-height:24px}
.price-box i{display:block;font-style:normal;font-size:15px;font-weight:700;line-height:17px}

/* package tiles */
.tile{position:absolute;width:92px;height:59px;border:1px solid var(--line);border-radius:5px;background:#fff}
.tile-ring{position:absolute;left:19px;top:-12px;width:48px;height:48px;border-radius:50%;border:3px solid var(--ink);background:#fff;overflow:hidden}
.tile-ring .product{position:absolute;inset:6px 2px;border-radius:3px;background:linear-gradient(180deg,#5a5a5a,#232323)}
.tile-label{position:absolute;left:6px;right:6px;bottom:-1px;height:13px;border-radius:7px;background:var(--grey);color:#fff;font-size:6.3px;font-weight:600;text-align:center;line-height:13px;white-space:nowrap;overflow:hidden}

/* inclusions */
.inclusions{position:absolute;left:265px;top:247px;width:215px;height:235px;background:var(--red);border-radius:4px 12px 12px 12px;padding:17px 10px 0 13px;list-style:none;color:#fff}
.inclusions li{position:relative;padding-left:14px;font-size:7.7px;font-weight:500;line-height:8px;margin-bottom:8.7px}
.inclusions li svg{position:absolute;left:0;top:0;width:8px;height:8px}

/* call to action */
.cta{position:absolute;width:212px}
.cta-also{position:absolute;left:0;top:0;font-size:19px;line-height:19px;font-weight:400}
.cta-offer{position:absolute;left:0;top:19px;font-size:19px;line-height:19px;font-weight:700}
.cta-free{position:absolute;right:0;top:-4px;font-size:44px;font-weight:800;color:var(--red);line-height:44px;letter-spacing:1px}
.cta-demo{position:absolute;left:0;top:46px;width:212px;height:31px;border:1px solid #8a8a8a;border-radius:4px;font-size:14px;font-weight:700;text-align:center;line-height:29px}

.phone{position:absolute;display:flex;align-items:center;gap:5px;color:var(--red);font-weight:700}
.phone svg{flex:none}
.contact{position:absolute;left:31px;top:572px;width:452px;display:flex;align-items:center;font-size:9.6px;white-space:nowrap}
.contact .quote{margin-right:auto}
.contact .item{display:flex;align-items:center;gap:3px;margin-left:6px;font-size:8px}

.maker{position:absolute;left:36px;top:605px;display:flex;align-items:center;gap:6px}
.maker-square{width:20px;height:20px;background:#2c5fb4}
.maker-name{font-size:10.5px;font-weight:400;color:#222}
.terms{position:absolute;left:188px;top:604px;width:292px;font-size:5.2px;line-height:6.8px;color:#222}

/* back page */
.back-hero{position:absolute;left:0;top:0;width:512px;height:242px;background:#000;overflow:hidden}
.gym-photo{position:absolute;left:190px;top:0;width:322px;height:242px;background:linear-gradient(180deg,#1a1c1c 0%,#3f5a45 28%,#6e8f6a 40%,#7c6a52 60%,#262626 100%)}
.gym-fade{position:absolute;left:190px;top:0;width:60px;height:242px;background:linear-gradient(90deg,#000,rgba(0,0,0,0))}
.gym-frame{position:absolute;left:284px;top:25px;width:195px;height:171px;border:1.5px solid #fff}
.why-title{position:absolute;left:26px;top:30px;color:#fff;font-size:14px;letter-spacing:3px;font-weight:500}
.why-sub{position:absolute;left:26px;top:47px;color:var(--red);font-size:11.6px;font-weight:700}
.why-copy{position:absolute;left:26px;width:228px;color:#fff;font-size:7.3px;line-height:9.1px;text-align:justify}
.why-copy--bold{font-weight:700}

.feature{position:absolute}
.feature-icon{position:absolute;left:-26px;top:0;width:19px;height:19px}
.feature h3{font-size:12.4px;font-weight:700;line-height:14.5px}
.feature p{margin-top:4px;font-size:6.9px;line-height:8.5px;text-align:justify}
</style>
</head>
<body>

<!-- FRONT PAGE -->
<section class="page page--front" aria-label="Flyer page one">
  <div class="hero">
    <div class="hero-photo" role="img" aria-label="Photo of a school hall with a large LED video wall mounted on the wall"></div>
    <div class="hero-screen" role="img" aria-label="Night city skyline shown on the video wall"></div>
    <svg class="hero-shape" width="512" height="234" viewBox="0 0 512 234">
      <defs>
        <linearGradient id="darkFade" x1="0" y1="0" x2="0" y2="1">
          <stop offset="0" stop-color="#262626"/><stop offset="1" stop-color="#1a1a1a"/>
        </linearGradient>
      </defs>
      <polygon points="0,0 280,0 233,234 0,234" fill="url(#darkFade)"/>
      <polygon points="280,0 292,0 245,234 233,234" fill="#fff"/>
    </svg>
    <div class="brand-mark">PRISM</div>
    <div class="brand-sub">LED VIDEO WALL</div>
    <div class="kicker">CUTTING EDGE</div>
    <div class="headline-brand">PRISM</div>
    <div class="headline-led">LED</div>
    <div class="headline-wall">VIDEO WALL</div>
    <div class="headline-for">FOR SCHOOLS</div>
  </div>

  <p class="price-lead">INCLUDING<br>INSTALLATION<br><span>FOR ONLY</span></p>
  <div class="price-box"><b>$35,500</b><i>EX TAX</i></div>

  <div class="tile" style="left:32px;top:314px"><div class="tile-ring"><div class="product" role="img" aria-label="Rack amplifier"></div></div><div class="tile-label">Amplifier</div></div>
  <div class="tile" style="left:145px;top:314px"><div class="tile-ring"><div class="product" role="img" aria-label="Video processor unit"></div></div><div class="tile-label">QT720 video processor</div></div>
  <div class="tile" style="left:32px;top:390px"><div class="tile-ring"><div class="product" style="background:linear-gradient(180deg,#cfcfcf,#9a9a9a)" role="img" aria-label="HDMI wall plate"></div></div><div class="tile-label">HDMI socke</div></div>
  <div class="tile" style="left:145px;top:390px"><div class="tile-ring"><div class="product" style="background:linear-gradient(90deg,#3f6fc0,#b88fe0)" role="img" aria-label="Box of cabling"></div></div><div class="tile-label">Cabling</div></div>
  <div class="tile" style="left:32px;top:474px"><div class="tile-ring"><div class="product" role="img" aria-label="Lockable wall cabinet"></div></div><div class="tile-label">Wall cabinet</div></div>
  <div class="tile" style="left:145px;top:474px"><div class="tile-ring"><div class="product" style="inset:3px 10px" role="img" aria-label="Speaker"></div></div><div class="tile-label">2 x speakers</div></div>

  <ul class="inclusions">
    <li><svg viewBox="0 0 10 10"><circle cx="5" cy="5" r="5" fill="#fff"/><path d="M2.8 5.1l1.5 1.5 2.9-3" stroke="#ed1c24" stroke-width="1.3" fill="none"/></svg>PRISM LED Video wall Display 4000mm wide x 2250mm high (157” or 4580mm diagonal)</li>
    <li><svg viewBox="0 0 10 10"><circle cx="5" cy="5" r="5" fill="#fff"/><path d="M2.8 5.1l1.5 1.5 2.9-3" stroke="#ed1c24" stroke-width="1.3" fill="none"/></svg>High resolution 2.6mm LED pitch</li>
    <li><svg viewBox="0 0 10 10"><circle cx="5" cy="5" r="5" fill="#fff"/><path d="M2.8 5.1l1.5 1.5 2.9-3" stroke="#ed1c24" stroke-width="1.3" fill="none"/></svg>Lumenar video processor</li>
    <li><svg viewBox="0 0 10 10"><circle cx="5" cy="5" r="5" fill="#fff"/><path d="M2.8 5.1l1.5 1.5 2.9-3" stroke="#ed1c24" stroke-width="1.3" fill="none"/></svg>250 Watt 4-channel Mixer amplifier</li>
    <li><svg viewBox="0 0 10 10"><circle cx="5" cy="5" r="5" fill="#fff"/><path d="M2.8 5.1l1.5 1.5 2.9-3" stroke="#ed1c24" stroke-width="1.3" fill="none"/></svg>2 x 10” full range professional speakers providing 250 watts RMS (including brackets)</li>
    <li><svg viewBox="0 0 10 10"><circle cx="5" cy="5" r="5" fill="#fff"/><path d="M2.8 5.1l1.5 1.5 2.9-3" stroke="#ed1c24" stroke-width="1.3" fill="none"/></svg>Lockable wall cabinet for hardware.</li>
    <li><svg viewBox="0 0 10 10"><circle cx="5" cy="5" r="5" fill="#fff"/><path d="M2.8 5.1l1.5 1.5 2.9-3" stroke="#ed1c24" stroke-width="1.3" fill="none"/></svg>HDMI input wall plate connection for Laptop / PC</li>
    <li><svg viewBox="0 0 10 10"><circle cx="5" cy="5" r="5" fill="#fff"/><path d="M2.8 5.1l1.5 1.5 2.9-3" stroke="#ed1c24" stroke-width="1.3" fill="none"/></svg>Fully installed and programmed</li>
    <li><svg viewBox="0 0 10 10"><circle cx="5" cy="5" r="5" fill="#fff"/><path d="M2.8 5.1l1.5 1.5 2.9-3" stroke="#ed1c24" stroke-width="1.3" fill="none"/></svg>Full user training</li>
    <li><svg viewBox="0 0 10 10"><circle cx="5" cy="5" r="5" fill="#fff"/><path d="M2.8 5.1l1.5 1.5 2.9-3" stroke="#ed1c24" stroke-width="1.3" fill="none"/></svg>Premium spare parts kit</li>
    <li><svg viewBox="0 0 10 10"><circle cx="5" cy="5" r="5" fill="#fff"/><path d="M2.8 5.1l1.5 1.5 2.9-3" stroke="#ed1c24" stroke-width="1.3" fill="none"/></svg>3 Year on Site Warranty</li>
  </ul>

  <div class="cta" style="left:267px;top:492px">
    <div class="cta-also">WE ALSO</div>
    <div class="cta-offer">OFFER A</div>
    <div class="cta-free">FREE</div>
    <div class="cta-demo">ON-SITE DEMONSTRATION</div>
  </div>

  <div class="phone" style="left:31px;top:546px;font-size:20px">
    <svg width="20" height="20" viewBox="0 0 20 20"><circle cx="10" cy="10" r="10" fill="#111"/><path d="M6.5 5.5c.6-.6 1.3-.5 1.7.1l1 1.5c.3.5.2 1-.2 1.4l-.6.5c.5 1.2 1.5 2.2 2.7 2.8l.5-.6c.4-.4 1-.5 1.4-.2l1.5 1c.6.4.7 1.1.1 1.7-1 1-2.3 1.2-4 .3-2-1.1-3.6-2.7-4.6-4.6-.9-1.7-.7-3 .5-3.9z" fill="#fff"/></svg>
    1300 555 019
  </div>

  <div class="contact">
    <span class="quote">or request a free quote below</span>
    <span class="item"><svg width="8" height="6" viewBox="0 0 8 6"><rect width="8" height="6" fill="#ed1c24"/><path d="M0 0l4 3.3L8 0" stroke="#fff" stroke-width=".8" fill="none"/></svg>prism@halvornworks.example.au</span>
    <span class="item"><svg width="9" height="9" viewBox="0 0 10 10"><circle cx="5" cy="5" r="4.3" stroke="#ed1c24" fill="none"/><ellipse cx="5" cy="5" rx="1.8" ry="4.3" stroke="#ed1c24" fill="none"/><path d="M.7 5h8.6" stroke="#ed1c24"/></svg>www.halvornworks.example.au</span>
  </div>

  <div class="maker"><span class="maker-square"></span><span class="maker-name">Halvorn signal works</span></div>
  <p class="terms">*Terms and conditions apply, installation subject to detailed site inspection for suitability of LED video wall. Installation excluding installation of power and height access equipment if required. Additional costs may apply for regional areas. Various sizes and resolutions available upon request. Educational finance package also available</p>
  <div class="footer-bar"></div>
</section>

<!-- BACK PAGE -->
<section class="page page--back" aria-label="Flyer page two">
  <div class="back-hero">
    <div class="gym-photo" role="img" aria-label="Photo of a school gymnasium with a PRISM LED video wall installed"></div>
    <div class="gym-fade"></div>
    <div class="gym-frame"></div>
    <svg class="abs" style="left:0;top:0" width="512" height="242" viewBox="0 0 512 242">
      <polygon points="264,242 276,216 512,216 512,242" fill="#ed1c24"/>
    </svg>
    <div class="why-title">WHY ARE SCHOOLS</div>
    <div class="why-sub">SELECTING PRISM LED VIDEO WALLS ?</div>
    <p class="why-copy" style="top:78px">Technology is changing at a rapid speed \and educational facilities need to continually evolve to ensure visual displays are capturing students attention with eye-catching and immersive visuals at all education levels. Traditional dull and washed out projectors offering poor images and no colour or vibrance are falling short on both performance and expectations for teachers and students.</p>
    <p class="why-copy why-copy--bold" style="top:154px">Our PRISM LED video walls represent a groundbreaking solution for schools seeking to elevate their learning environments. Unlike traditional projectors or LCD panels, our LED video walls offer unparalleled clarity, super high brightness and color accuracy, ensuring an immersive visual experience.</p>
  </div>

  <div class="feature" style="left:58px;top:265px;width:181px">
    <svg class="feature-icon" viewBox="0 0 20 20"><circle cx="10" cy="10" r="10" fill="#ed1c24"/><path d="M10 5v10M5 10h10M10 5l-1.5 1.5M10 5l1.5 1.5M15 10l-1.5-1.5M15 10l-1.5 1.5" stroke="#fff" stroke-width="1" fill="none"/></svg>
    <h3>FLEXIBILITY</h3>
    <p>PRISM LED video walls are assembled in modular sizes comprising of an engineered aluminum cabinet of 1000mm wide x 562mm high, they are an impressive 28mm in thickness and can be customised to suit your exact requirements, you can even add to your screen size later if you feel bigger is better later on down the track.</p>
  </div>

  <div class="feature" style="left:58px;top:363px;width:181px">
    <svg class="feature-icon" viewBox="0 0 20 20"><circle cx="10" cy="10" r="10" fill="#ed1c24"/><rect x="5" y="6.5" width="10" height="7" rx="1" stroke="#fff" fill="none"/><circle cx="10" cy="10" r="1.6" stroke="#fff" fill="none"/></svg>
    <h3>SUPERIOR VISUAL<br>EXPERIENCE</h3>
    <p>Each LED pixel functions independently, delivering outstanding image quality with true-to-life color depiction. Regardless of ambient light conditions, our LED displays provide exceptional visibility and clarity, making them perfect for brightly lit environments such as school gymnasiums and auditoriums.</p>
  </div>

  <div class="feature" style="left:287px;top:260px;width:194px">
    <svg class="feature-icon" style="left:-25px" viewBox="0 0 20 20"><circle cx="10" cy="10" r="10" fill="#ed1c24"/><circle cx="10" cy="10" r="4.5" stroke="#fff" fill="none"/><circle cx="10" cy="10" r="2" stroke="#fff" fill="none"/></svg>
    <h3>IMPACT RESISTANT</h3>
    <p>Every single PRISM LED video wall cabinet has eight precision LED modules attached with an array of high-strength magnets requiring a service tool for removal (included), each LED is also protected by a mesh insert and finally, every single LED module is secured with a safety tether to ensure in the event that a module is dislodged that it will not fall more than a few inches thus preventing injury and damage to any module. Impact from balls such as tennis balls, volleyballs etc are unlikely to cause any damage to the PRISM LED video wall.</p>
  </div>

  <div class="feature" style="left:287px;top:390px;width:194px">
    <svg class="feature-icon" style="left:-25px" viewBox="0 0 20 20"><circle cx="10" cy="10" r="10" fill="#ed1c24"/><path d="M10 5v10M5 10h10" stroke="#fff"/><circle cx="10" cy="5.5" r="1.2" fill="#fff"/><circle cx="10" cy="14.5" r="1.2" fill="#fff"/><circle cx="5.5" cy="10" r="1.2" fill="#fff"/><circle cx="14.5" cy="10" r="1.2" fill="#fff"/></svg>
    <h3>VERSATILITY<br>&amp; INTEGRATION</h3>
    <p>Our LED displays offer seamless integration with existing IT systems, we include a long range HDMI input connection for Laptops, you can also add wireless microphones, devices such as Castly, BeamLink, and additional video, digital signage, scoreboard software or Laptop inputs. This allows for easy integration within school networks and facilitates features like screen casting and screen sharing, enhancing collaboration and inclusivity in the learning process.</p>
  </div>

  <div class="cta" style="left:32px;top:486px;width:208px">
    <div class="cta-also">WE ALSO</div>
    <div class="cta-offer">OFFER A</div>
    <div class="cta-free">FREE</div>
    <div class="cta-demo" style="width:208px">ON-SITE DEMONSTRATION</div>
  </div>

  <div class="phone" style="left:261px;top:527px;font-size:28px;gap:12px">
    <svg width="27" height="27" viewBox="0 0 20 20"><circle cx="10" cy="10" r="10" fill="#111"/><path d="M6.5 5.5c.6-.6 1.3-.5 1.7.1l1 1.5c.3.5.2 1-.2 1.4l-.6.5c.5 1.2 1.5 2.2 2.7 2.8l.5-.6c.4-.4 1-.5 1.4-.2l1.5 1c.6.4.7 1.1.1 1.7-1 1-2.3 1.2-4 .3-2-1.1-3.6-2.7-4.6-4.6-.9-1.7-.7-3 .5-3.9z" fill="#fff"/></svg>
    1300 555 019
  </div>

  <div class="contact" style="left:32px;width:451px">
    <span class="quote">or request a free quote below</span>
    <span class="item"><svg width="8" height="6" viewBox="0 0 8 6"><rect width="8" height="6" fill="#ed1c24"/><path d="M0 0l4 3.3L8 0" stroke="#fff" stroke-width=".8" fill="none"/></svg>prism@halvornworks.example.au</span>
    <span class="item"><svg width="9" height="9" viewBox="0 0 10 10"><circle cx="5" cy="5" r="4.3" stroke="#ed1c24" fill="none"/><ellipse cx="5" cy="5" rx="1.8" ry="4.3" stroke="#ed1c24" fill="none"/><path d="M.7 5h8.6" stroke="#ed1c24"/></svg>www.halvornworks.example.au</span>
  </div>

  <div class="maker"><span class="maker-square"></span><span class="maker-name">Halvorn signal works</span></div>
  <p class="terms">*Terms and conditions apply, installation subject to detailed site inspection for suitability of LED video wall. Installation excluding installation of power and height access equipment if required. Additional costs may apply for regional areas. Various sizes and resolutions available upon request. Educational finance package also available</p>
  <div class="footer-bar"></div>
</section>

</body>
</html>
```